MOVEMENT TO STOP ILLEGAL PARTIES IN VILLAS IBIZA

We are a tourist villa management company in Ibiza, we advertise photos of the villas on pages such as STAYNEST.COM or LODGEVA. We want to take a photo, the technical quality requirements can be seen in the following example "picture example requirements", the image will be included within the images of each house in the LODGEVA and STAYNEST.COM ads, etc. It is an image that we want to give a message that we belong to a movement: MOVEMENT STOP ILLEGAL PARTIES IN VILLAS IBIZA, we want to give the following message:
1 RESPECT THE NEIGHBORS. linked to the attached image of a person who does yoga in front of the sea, an image of relaxation and enjoyment without loud music and disturbing neighbors,
2. MOVEMENT STOP ILLEGAL PARTIES IN VILLAS IBIZA linked to images of police and security guards.
3. ¡¡24 hour loud sound control system¡¡ linked to the image of alarm detectors.
These images and messages need to be combined to deter party planners from booking this home while not hurting new bookings from good clients who want to enjoy the home. The image has to be pleasant but have a clear message, that there is no doubt that the house has an alarm to detect loud sounds and quickly notify the owners, the marketing agency and the police.

We want that when you see the house you DO NOT make reservations if your intention is to have a party at the house, invite a lot of people, charge tickets, play very loud music, sell drugs...

Target Market(s)

Vacational rental guests in Ibiza

Industry/Entity Type

Turismo

Requirements
Must have
• Clear message, avoid reservations in geste villas that want to have a party.
Should not have
• Jokes, humor, must be serious.

```html
<!DOCTYPE html>
<html lang="en">
<head>
<meta charset="utf-8">
<title>Stop Illegal Parties in Villas Ibiza</title>
<link rel="stylesheet" href="https://fonts.googleapis.com/css2?family=Montserrat:wght@500;600;700;800;900&display=swap">
<style>
  :root{
    --bg:#d6d7db;
    --red:#b8121c;
    --red-dark:#8e0c14;
    --red-text:#c4151f;
    --white:#ffffff;
    --ink:#111111;
    --teal:#16a8b6;
    --teal-dark:#0f7f8c;
    --blue:#1f86d4;
    --black:#0b0b0b;
  }
  *{margin:0;padding:0;box-sizing:border-box}
  html,body{width:1200px;height:1177px;overflow:hidden;background:var(--bg)}
  body{position:relative;font-family:'Montserrat',sans-serif;color:var(--ink)}

  .flyer{
    position:absolute;left:223px;top:102px;width:628px;height:810px;
    transform:scale(1.2);transform-origin:0 0;
    background:var(--white);overflow:hidden;
  }
  .flyer > *{position:absolute}

  .villa-photo{left:0;top:0;width:628px;height:252px;
    background:linear-gradient(180deg,#2f7fd6 0%,#6fa6d8 28%,#5f7d48 52%,#8c8a72 78%,#3f8fcf 100%)}

  .hero-band{left:0;top:250px;width:628px;height:165px;
    background:linear-gradient(180deg,var(--red) 0%,var(--red-dark) 100%)}

  .guard-photo{left:12px;top:155px;width:276px;height:260px;
    background:linear-gradient(180deg,#5d6670 0%,#2a2d33 55%,#1a1c20 100%)}

  .hero-title{left:288px;top:226px;width:330px;text-align:center;color:var(--white)}
  .hero-title .stop{display:block;font-size:92px;font-weight:900;line-height:1;letter-spacing:1px;
    text-shadow:0 0 0 var(--red),3px 3px 0 var(--red),-3px -3px 0 var(--red),3px -3px 0 var(--red),-3px 3px 0 var(--red)}
  .hero-title .line{display:block;font-size:27px;font-weight:800;line-height:1.2;margin-top:4px}
  .hero-title .line + .line{margin-top:0}
  .hero-rule{left:308px;top:395px;width:292px;height:3px;background:var(--white)}

  .neighbours-photo{left:0;top:415px;width:230px;height:167px;
    clip-path:polygon(0 0,100% 0,88% 100%,0 100%);
    background:linear-gradient(180deg,#4aa3e6 0%,#8fc1e6 35%,#2f6fa6 60%,#c9a77b 100%)}

  .section-head{left:196px;top:418px;width:432px;height:48px;
    clip-path:polygon(8% 0,100% 0,100% 100%,0 100%);
    background:linear-gradient(90deg,var(--teal) 0%,#1e9bd4 100%);
    border-top:4px solid var(--teal-dark);
    display:flex;align-items:center;justify-content:center;padding-left:20px;
    color:var(--white);font-size:25px;font-weight:800}

  .neighbours-copy{left:226px;top:474px;width:398px;text-align:center;font-size:15px;font-weight:600;line-height:1.3}
  .neighbours-copy strong{color:var(--red-text);font-weight:900}

  .warning{left:243px;top:516px;width:375px;height:54px;border:2px solid var(--red-text);border-radius:24px;
    display:flex;align-items:center;gap:8px;padding:0 12px 0 6px}
  .warning svg{flex:0 0 auto}
  .warning p{font-size:11.5px;font-weight:600;line-height:1.25}
  .warning strong{color:var(--red-text);font-weight:900}

  .alarm-head{left:0;top:582px;width:380px;height:74px;background:var(--black);
    clip-path:polygon(0 0,100% 0,88% 100%,0 100%);
    padding:6px 0 0 14px;font-size:25px;font-weight:900;line-height:1.25;color:var(--white)}
  .alarm-head .accent{color:var(--red-text);display:block}

  .devices-photo{left:14px;top:662px;width:132px;height:125px;
    background:radial-gradient(circle at 50% 25%,#f2f2f2 0%,#dcdde0 60%,#c6c8cc 100%)}

  .alarm-copy{left:154px;top:672px;width:168px;font-size:15px;font-weight:600;line-height:1.2}
  .alarm-copy strong{color:var(--red-text);font-weight:900}

  .police-photo{left:322px;top:582px;width:306px;height:216px;
    clip-path:polygon(18% 0,100% 0,100% 100%,0 100%);
    background:linear-gradient(180deg,#7c8a6e 0%,#4d5a4a 40%,#b8bfc6 75%,#8a949c 100%)}

  .footer-strip{left:0;top:798px;width:628px;height:12px;background:var(--blue)}
</style>
</head>
<body>
  <div class="flyer">
    <div class="villa-photo" role="img" aria-label="Villa terrace with pool, pergola and sun loungers under a blue sky and wooded hills"></div>
    <div class="hero-band"></div>
    <div class="guard-photo" role="img" aria-label="Security guard in cap and sunglasses holding up an open hand to signal stop"></div>
    <h1 class="hero-title">
      <span class="stop">STOP</span>
      <span class="line">ILLEGAL PARTIES</span>
      <span class="line">IN VILLAS IBIZA</span>
    </h1>
    <div class="hero-rule"></div>

    <div class="neighbours-photo" role="img" aria-label="Woman meditating on rocks in front of the sea and island cliffs"></div>
    <h2 class="section-head">Respect The Neighbours</h2>
    <p class="neighbours-copy">Relaxation &amp; enjoyment <strong>WITHOUT</strong> loud music and disturbing neighbors,</p>
    <div class="warning">
      <svg width="34" height="34" viewBox="0 0 34 34" aria-hidden="true">
        <circle cx="17" cy="17" r="16" fill="#c4151f"/>
        <rect x="15" y="7" width="4" height="14" rx="2" fill="#fff"/>
        <circle cx="17" cy="26" r="2.4" fill="#fff"/>
      </svg>
      <p><strong>DO NOT MAKE RESERVATIONS</strong> if your intention is to have a party at the house, invite a lot of people, play very loud music, sell drugs...</p>
    </div>

    <h2 class="alarm-head"><span class="accent">24 Hour Loud Sound</span>CONTROL SYSTEM</h2>
    <div class="devices-photo" role="img" aria-label="White alarm kit: siren, motion sensors, door contact and remote control"></div>
    <p class="alarm-copy">This house has an alarm to detect loud sounds and <strong>QUICKLY NOTIFY</strong> the owners, the marketing agency and the police.</p>
    <div class="police-photo" role="img" aria-label="Police officers and patrol car at a villa gate"></div>

    <div class="footer-strip"></div>
  </div>
</body>
</html>
```